Velvet Crest Car Detailing Brochure

I would like a trifold brochure designed for my car detailing business. The background has to be full black or mostly black with some designing using only colors present in our logo.

Front page must have our logo and name, list of services, a photo and mybe our phone number but no long text.

Inside I want to present each service one by one with its description and a photo representing/showing each service. (I will provide the text below). For photos, use stock photos and I will add come of mines already too.

On the back of the brochure I want to have contact & info: phone number, opening hours, address, website, Instagram.

Outside left I want the text About us and photo/design.

I want the brochure to be neat, professional, easy to read, but at the same time not too boring.

Text:
1. About us
a. the ultimate destination for car care in Geneva. We provide personalized, detail-oriented services that bring out the best in your car. With our expert techniques and dedicated approach, we ensure that your car receives the utmost care and attention. Experience a place where passion meets precision and let us create an exceptional car care experience designed just for you.
2. Services:

DETAILING & HAND WASH

• Comprehensive exterior & interior care
• Personalisation and tailored cleaning packages
• Decontamination
• Premium products
• Attention to detail for a perfect finish

POLISHING

• Eliminates scratches, holograms
• Revives and protects paint
• Ensures lasting gloss
• Enhances paint life
• Preserves car’s value and beauty

CERAMIC TREATMENT

• Durable paint protection
• Water-repellent (hydrophobic) effect
• Easier cleaning, enhanced shine
• Long-term surface safeguarding
• Shields against environmental impacts

DRY ICE WASH

• Innovative, waterless method
• Safe for all car parts
• Deep cleans, removes odors
• Allergen-free, antibacterial
• Gentle, effective
• Advanced cleaning technology

COVERING

• Personalized vehicle styling
• More than 150 colours available
• Clean cut without using a cutter
• High-quality, durable materials
• Custom designs available

PROTECTION FILM

• Invisible, durable shield
• Self-healing technology
• 10-year warranty by QR VONT

DETAILING BOUTIQUE

• Premium brands available
• Buy on site during your visit
• Marble Harbour, Zeb Autos, DRUP Polaro
• Essential for at-home car care
• Perfect for quick touch-ups
(for these three brands you can put their logos

Target Market(s)

Our target market includes car owners of all price ranges, with a special focus on those who are passionate about their vehicles. We cater to clients who value excellent service and results, and seek to maintain their cars in pristine condition.

Industry/Entity Type

Automobile / Car detailing

Colors

Designer to choose colors to be used in the design.

Requirements
Must have
• Brand Consistency: The brochure must adhere to our brand colors and style, particularly utilizing the colors present in our logo. Trifold Layout: The design must be specifically tailored for a trifold brochure format. Legibility: Text must be easy to read against the mostly black background, with appropriate font size and style. Professional Look and Feel: The overall design must convey professionalism while being engaging and not overly complex. Photo representation: each service description should have a phot presenting it.
Should not have
• Overcrowded Design: Avoid cluttering with too much text or too many images. The layout should be clean and easy to navigate. Cartoonish Fonts or Graphics: Avoid using unprofessional or casual fonts and graphics that do not align with the upscale and professional image of our business. Distracting Backgrounds: The background should complement and not overpower the content. Stick to the theme of mostly black with design elements from our logo.

```html
<!DOCTYPE html>
<html lang="en">
<head>
<meta charset="utf-8">
<title>Velvet Crest Car Detailing – Trifold Brochure</title>
<link rel="stylesheet" href="https://fonts.googleapis.com/css2?family=Lato:wght@400;700&family=Barlow+Semi+Condensed:wght@400;500;600&display=swap">
<style>
  :root{
    --stage:#2f2f32;
    --ink:#0a0a0c;
    --paper:#f2f2f3;
    --white:#ffffff;
    --text-dark:#2b2b2e;
    --blue:#2b9fdc;
    --pink:#e2308e;
    --purple:#8a4fc9;
    --line-blue:#2a6fc0;
    --photo-a:#3d3f44;
    --photo-b:#17181b;
    --body:"Lato", Arial, sans-serif;
    --cond:"Barlow Semi Condensed", "Arial Narrow", sans-serif;
  }
  *{margin:0;padding:0;box-sizing:border-box}
  html,body{width:887px;height:1200px;overflow:hidden}
  body{background:var(--stage);position:relative;font-family:var(--body);color:var(--white)}

  .sheet{position:absolute;left:84px;width:724px;height:513px;background:var(--ink);overflow:hidden}
  .sheet--outside{top:75px}
  .sheet--inside{top:623px}

  /* ---------- outside ---------- */
  .hero-photo{position:absolute;left:243px;top:0;width:481px;height:513px;
    background:
      radial-gradient(ellipse 60% 22% at 70% 60%, #5b5d63 0%, rgba(40,40,44,0) 70%),
      linear-gradient(170deg,#2a2b2f 0%,#0d0d10 28%,#121316 55%,#050506 100%)}
  .band{position:absolute;inset:0}
  .about{position:absolute;left:0;top:0;width:243px;height:513px;background:var(--paper);color:var(--text-dark)}
  .about__corner{position:absolute;left:0;top:0}
  .brand-mini{position:absolute;left:78px;top:32px;width:70px;height:70px;border-radius:50%;
    border:3px solid var(--pink);background:var(--white);display:flex;align-items:center;justify-content:center;
    font-family:var(--body);font-weight:700;font-size:9px;color:var(--pink);text-align:center;line-height:1.15;letter-spacing:.5px}
  .about__title{position:absolute;left:0;width:243px;top:112px;text-align:center;font-size:21px;line-height:24px;font-weight:400;color:#1f1f22;text-transform:uppercase}
  .about__title .accent{display:block;color:var(--blue);font-size:37px;line-height:40px}
  .about__place{position:absolute;left:14px;width:215px;top:203px;display:flex;align-items:center;gap:6px;font-size:9px;letter-spacing:.5px;color:#1f1f22}
  .about__place::before,.about__place::after{content:"";flex:1;height:1px;background:var(--pink)}
  .about__text{position:absolute;left:14px;width:216px;font-size:10px;line-height:12.6px;text-align:justify;color:#333}
  .about__text--a{top:226px}
  .about__text--b{top:292px}
  .about__photo{position:absolute;left:0;top:355px;width:243px;height:158px;
    background:linear-gradient(135deg,#c9cbcf 0%,#8f9196 45%,#3e4045 100%)}

  .contact{position:absolute;left:271px;top:130px;width:170px;font-size:9.5px;line-height:12px}
  .contact__lead{margin-bottom:12px}
  .contact__row{display:flex;gap:7px;align-items:flex-start;margin-bottom:2px}
  .contact__row svg{flex:none;margin-top:1px}
  .contact__gap{height:8px}
  .contact__hours{margin-top:12px;color:var(--blue);font-weight:700;font-size:9px;letter-spacing:.3px}

  .brand{position:absolute;left:520px;top:14px;width:160px;text-align:center}
  .brand__ring{display:block;margin:0 auto 12px;width:110px;height:110px;border-radius:50%;border:4px solid var(--purple)}
  .brand__name{font-family:var(--body);font-size:22px;line-height:27px;font-weight:400;letter-spacing:.5px;color:var(--white);text-transform:uppercase}

  .phone-badge{position:absolute;left:484px;top:414px;width:108px;height:30px;background:var(--blue);
    transform:rotate(-20.8deg) skewX(-8deg);display:flex;align-items:center;justify-content:center}
  .phone-badge span{transform:skewX(8deg);font-family:var(--cond);font-weight:600;font-size:17px;letter-spacing:.5px;color:var(--ink)}
  .phone-dot{position:absolute;left:519px;top:385px;width:18px;height:18px;border-radius:50%;background:var(--ink);display:flex;align-items:center;justify-content:center}

  .service-list{position:absolute;left:598px;top:402px;list-style:none;font-family:var(--cond);font-size:9.5px;line-height:13.7px;letter-spacing:.2px;text-transform:uppercase}
  .service-list li{position:relative;padding-left:9px}
  .service-list li::before{content:"";position:absolute;left:0;top:4px;border-left:5px solid var(--pink);border-top:3px solid transparent;border-bottom:3px solid transparent}

  .web{position:absolute;left:340px;top:468px;width:160px;text-align:center;font-size:9.5px;letter-spacing:.3px}
  .web svg{display:block;margin:0 auto 4px}

  /* ---------- inside ---------- */
  .inside-deco{position:absolute;inset:0}
  .card{position:absolute;border:1px solid var(--line-blue)}
  .card__title{position:absolute;left:8px;right:-1px;top:9px;height:20px;
    background:linear-gradient(90deg,var(--blue) 0%,var(--purple) 60%,var(--pink) 100%);
    font-family:var(--cond);font-weight:600;font-size:12.5px;line-height:20px;text-align:center;color:var(--white);letter-spacing:.3px;text-transform:uppercase}
  .card__photo{position:absolute;background:linear-gradient(160deg,var(--photo-a) 0%,var(--photo-b) 100%)}
  .card__list{position:absolute;list-style:none;font-family:var(--cond);font-size:9.5px;line-height:11.2px;color:var(--white)}
  .card__list li{position:relative;padding-left:7px}
  .card__list li::before{content:"•";position:absolute;left:0}

  .card--tall{width:211px;height:231px}
  .card--tall .card__photo{top:39px;width:98px;height:177px}
  .card--tall.card--photo-left .card__photo{left:9px}
  .card--tall.card--photo-left .card__list{left:107px;top:42px;width:98px}
  .card--tall.card--photo-right .card__photo{left:104px}
  .card--tall.card--photo-right .card__list{left:9px;top:42px;width:94px}

  .card--short{width:211px;height:151px}
  .card--short .card__photo{left:9px;top:36px;width:94px;height:101px}
  .card--short .card__list{left:108px;top:38px;width:100px}
</style>
</head>
<body>

<!-- OUTSIDE: about / contact / cover -->
<section class="sheet sheet--outside" aria-label="Brochure outside">
  <div class="hero-photo" role="img" aria-label="Glossy black sports car in side profile on a dark studio background with soft light streaks"></div>

  <svg class="band" width="724" height="513" viewBox="0 0 724 513" aria-hidden="true">
    <polygon points="243,513 724,328 724,513" fill="#0a0a0c"/>
    <polygon points="236,513 724,325 724,332 252,513" fill="#2b9fdc"/>
  </svg>

  <div class="about">
    <svg class="about__corner" width="243" height="100" viewBox="0 0 243 100" aria-hidden="true">
      <polygon points="0,0 248,0 0,93" fill="#0a0a0c"/>
      <polygon points="0,93 248,0 243,0 243,4 0,98" fill="#e2308e"/>
    </svg>
    <div class="brand-mini">VELVET<br>CREST</div>
    <h1 class="about__title">The Ultimate<br>Destination for<span class="accent">Car Care</span></h1>
    <div class="about__place">IN GENEVA</div>
    <p class="about__text about__text--a">We provide personalized, detail-oriented services that bring out the best in your car. With our expert techniques and dedicated approach, we ensure that your car receives the utmost care and attention.</p>
    <p class="about__text about__text--b">Experience a place where passion meets precision and let us create an exceptional car care experience designed just for you.</p>
    <div class="about__photo" role="img" aria-label="Detailer in black gloves hand-polishing the bonnet of a silver car with an applicator pad"></div>
  </div>

  <div class="contact">
    <p class="contact__lead">Should you have any queries or questions, please do not hesitate to contact us</p>
    <div class="contact__row">
      <svg width="8" height="10" viewBox="0 0 8 10"><path d="M4 0a4 4 0 0 1 4 4c0 3-4 6-4 6S0 7 0 4a4 4 0 0 1 4-4z" fill="#2b9fdc"/><circle cx="4" cy="4" r="1.5" fill="#0a0a0c"/></svg>
      <span>Address<br>Address<br>Geneva</span>
    </div>
    <div class="contact__gap"></div>
    <div class="contact__row">
      <svg width="8" height="9" viewBox="0 0 8 9"><path d="M1.5 0h1.6l.8 2.2-1 .8a5 5 0 0 0 2.1 2.1l.8-1L8 5v1.6c0 .8-.7 1.4-1.5 1.3C3.2 7.5.5 4.8.1 1.5 0 .7.7 0 1.5 0z" fill="#2b9fdc"/></svg>
      <span>+975318642</span>
    </div>
    <div class="contact__row">
      <svg width="9" height="8" viewBox="0 0 9 8"><rect x="0" y="1" width="9" height="6" rx="1" fill="#2b9fdc"/><path d="M0.5 1.5 4.5 4.5 8.5 1.5" stroke="#0a0a0c" stroke-width=".8" fill="none"/></svg>
      <span>contact@velvetcrest.com</span>
    </div>
    <div class="contact__row">
      <svg width="8" height="8" viewBox="0 0 8 8"><circle cx="4" cy="4" r="3.6" fill="#2b9fdc"/><path d="M.4 4h7.2M4 .4c-2 2-2 5.2 0 7.2M4 .4c2 2 2 5.2 0 7.2" stroke="#0a0a0c" stroke-width=".6" fill="none"/></svg>
      <span>www.velvetcrest.com</span>
    </div>
    <p class="contact__hours">OPENING HOUR</p>
  </div>

  <div class="brand">
    <span class="brand__ring" aria-hidden="true"></span>
    <p class="brand__name">Velvet<br>Crest</p>
  </div>

  <div class="phone-dot" aria-hidden="true">
    <svg width="9" height="9" viewBox="0 0 8 9"><path d="M1.5 0h1.6l.8 2.2-1 .8a5 5 0 0 0 2.1 2.1l.8-1L8 5v1.6c0 .8-.7 1.4-1.5 1.3C3.2 7.5.5 4.8.1 1.5 0 .7.7 0 1.5 0z" fill="#e2308e"/></svg>
  </div>
  <div class="phone-badge"><span>975318642</span></div>

  <ul class="service-list">
    <li>Detailing &amp; Hand Wash</li>
    <li>Polishing</li>
    <li>Ceramic Treatment</li>
    <li>Dry Ice Wash</li>
    <li>Covering</li>
    <li>Protection Film</li>
    <li>Detailing Boutique</li>
  </ul>

  <div class="web">
    <svg width="13" height="13" viewBox="0 0 8 8"><circle cx="4" cy="4" r="3.6" fill="#e2308e"/><path d="M.4 4h7.2M4 .4c-2 2-2 5.2 0 7.2M4 .4c2 2 2 5.2 0 7.2" stroke="#0a0a0c" stroke-width=".6" fill="none"/></svg>
    VELVETCREST.COM
  </div>
</section>

<!-- INSIDE: services -->
<section class="sheet sheet--inside" aria-label="Brochure inside">
  <svg class="inside-deco" width="724" height="513" viewBox="0 0 724 513" aria-hidden="true">
    <polygon points="0,0 230,0 0,42" fill="#2b9fdc"/>
    <polygon points="724,447 724,513 492,513" fill="#e2308e"/>
  </svg>

  <article class="card card--tall card--photo-left" style="left:14px;top:17px">
    <h2 class="card__title">Detailing &amp; Hand Wash</h2>
    <div class="card__photo" role="img" aria-label="Foam wash mitt cleaning a soapy car wheel"></div>
    <ul class="card__list">
      <li>Comprehensive exterior &amp; interior care</li>
      <li>Personalisation and tailored cleaning packages</li>
      <li>Decontamination</li>
      <li>Premium products</li>
      <li>Attention to detail for a perfect finish</li>
    </ul>
  </article>

  <article class="card card--tall card--photo-left" style="left:14px;top:262px">
    <h2 class="card__title">Dry Ice Wash</h2>
    <div class="card__photo" role="img" aria-label="Dry ice blasting machine releasing white vapour in a workshop"></div>
    <ul class="card__list">
      <li>Innovative, waterless method</li>
      <li>Safe for all car parts</li>
      <li>Deep cleans, removes odors</li>
      <li>Allergen-free, antibacterial</li>
      <li>Gentle, effective</li>
      <li>Advanced cleaning technology</li>
    </ul>
  </article>

  <article class="card card--short" style="left:257px;top:17px">
    <h2 class="card__title">Ceramic Treatment</h2>
    <div class="card__photo" role="img" aria-label="Gloved hand applying ceramic coating to a car panel"></div>
    <ul class="card__list">
      <li>Durable paint protection</li>
      <li>Water-repellent (hydrophobic) effect</li>
      <li>Easier cleaning, enhanced shine</li>
      <li>Long-term surface safeguarding</li>
      <li>Shields against environmental impacts</li>
    </ul>
  </article>

  <article class="card card--short" style="left:257px;top:181px">
    <h2 class="card__title">Ceramic Treatment</h2>
    <div class="card__photo" role="img" aria-label="Vinyl wrap being stretched over a car body"></div>
    <ul class="card__list">
      <li>Personalized vehicle styling</li>
      <li>More than 150 colours available</li>
      <li>Clean cut without using a cutter</li>
      <li>High-quality, durable materials</li>
      <li>Custom designs available</li>
    </ul>
  </article>

  <article class="card card--short" style="left:257px;top:344px">
    <h2 class="card__title">Protection Film</h2>
    <div class="card__photo" role="img" aria-label="Protection film roll and tools laid out in a bright studio"></div>
    <ul class="card__list" style="top:44px">
      <li>Invisible, durable shield</li>
      <li>Self-healing technology</li>
      <li>10-year warranty by QR VONT</li>
    </ul>
  </article>

  <article class="card card--tall card--photo-right" style="left:499px;top:17px">
    <h2 class="card__title">Polishing</h2>
    <div class="card__photo" role="img" aria-label="Blue rotary polisher working on a taped car panel"></div>
    <ul class="card__list">
      <li>Eliminates scratches, holograms</li>
      <li>Revives and protects paint</li>
      <li>Ensures lasting gloss</li>
      <li>Enhances paint life</li>
      <li>Preserves car's value and beauty</li>
    </ul>
  </article>

  <article class="card card--tall card--photo-right" style="left:499px;top:262px">
    <h2 class="card__title">Detailing Boutique</h2>
    <div class="card__photo" role="img" aria-label="Hands holding a polisher and care product bottles"></div>
    <ul class="card__list">
      <li>Premium brands available</li>
      <li>Buy on site during your visit</li>
      <li>Marble Harbour, Zeb Autos, DRUP Polaro</li>
      <li>Essential for at-home car care</li>
      <li>Perfect for quick touch-ups (for these three brands you can put their logos</li>
    </ul>
  </article>
</section>

</body>
</html>
```